need eczema bath soak label/bag

need you to recreate this please. ai file. recreate this exact image please. ...if you want a big tip, create some different styles.

Colors
0054AA
0677BA
7BADD7
CADEEF
E8F1F8

```html
<!DOCTYPE html>
<html lang="en">
<head>
<meta charset="utf-8">
<title>Ocean Healed Bath Soak Pouch</title>
<link rel="stylesheet" href="https://fonts.googleapis.com/css2?family=Barlow+Semi+Condensed:wght@600&family=Poppins:wght@400;600&display=swap">
<style>
  :root {
    --backdrop: #b4b4ae;
    --ink: #1d3534;
    --ocean-deep: #2aa3b2;
    --ocean-bright: #5fd3de;
    --foam: #eef5f8;
    --sand: #cdb08c;
    --zip: #3fb4c2;
  }
  * { margin: 0; padding: 0; box-sizing: border-box; }
  html, body { width: 1200px; height: 1108px; overflow: hidden; }
  body { background: var(--backdrop); position: relative; font-family: "Poppins", sans-serif; }

  .pouch {
    position: absolute; left: 296px; top: 169px;
    width: 604px; height: 767px; overflow: hidden;
    background: var(--sand);
  }
  .pouch__ocean {
    position: absolute; left: 0; top: 0; width: 100%; height: 490px;
    background: linear-gradient(180deg, var(--ocean-deep) 0%, var(--ocean-bright) 35%, #a9e3ea 60%, var(--foam) 80%, #f4f8fa 100%);
  }
  .pouch__sand {
    position: absolute; left: 0; top: 462px; width: 100%; height: 305px;
  }
  .pouch__zip {
    position: absolute; left: 34px; right: 34px; top: 82px; height: 20px;
    border-top: 2px solid var(--zip); border-bottom: 2px solid var(--zip);
    opacity: .8;
  }
  .pouch__notch {
    position: absolute; top: 36px; width: 10px; height: 8px; background: var(--backdrop);
  }
  .pouch__notch--left { left: 0; clip-path: polygon(0 0, 100% 50%, 0 100%); }
  .pouch__notch--right { right: 0; clip-path: polygon(100% 0, 0 50%, 100% 100%); }

  .headline {
    font-family: "Barlow Semi Condensed", sans-serif; font-weight: 600;
    color: var(--ink);
  }
  .headline__lead, .headline__line {
    position: absolute; left: 0; width: 100%; text-align: center; display: block;
    line-height: 1; white-space: nowrap;
  }
  .headline__lead { top: 152px; font-size: 36px; }
  .headline__line { font-size: 68px; letter-spacing: 1px; }
  .headline__line--ocean { top: 190px; }
  .headline__line--healed { top: 259px; }
  .headline__line--bag { top: 324px; }

  .blurb {
    position: absolute; left: 0; width: 100%; top: 398px; text-align: center;
    font-size: 8.8px; line-height: 13px; letter-spacing: .2px;
    color: var(--ink); text-transform: uppercase;
  }

  .brand {
    position: absolute; left: 0; width: 100%; top: 612px; text-align: center;
    font-size: 13px; font-weight: 600; letter-spacing: 5px; color: var(--ink);
  }
  .product-line {
    position: absolute; left: 0; width: 100%; top: 656px; text-align: center;
    font-size: 13px; font-weight: 600; letter-spacing: .8px; color: var(--ink);
  }
  .product-code {
    position: absolute; left: 0; width: 100%; top: 676px; text-align: center;
    font-family: "Barlow Semi Condensed", sans-serif; font-weight: 600;
    font-size: 22px; letter-spacing: 1px; color: var(--ink);
  }
  .product-type {
    position: absolute; left: 0; width: 100%; top: 709px; text-align: center;
    font-size: 7px; letter-spacing: 1px; color: var(--ink);
  }
</style>
</head>
<body>
  <main class="pouch">
    <div class="pouch__ocean" role="img" aria-label="Aerial photograph of turquoise ocean water with white surf"></div>
    <svg class="pouch__sand" viewBox="0 0 604 305" preserveAspectRatio="none" role="img" aria-label="Photograph of fine beach sand">
      <defs>
        <linearGradient id="sandTone" x1="0" y1="0" x2="0" y2="1">
          <stop offset="0" stop-color="#d8bf9c"/>
          <stop offset="1" stop-color="#c9ab85"/>
        </linearGradient>
      </defs>
      <path d="M0 26 C40 12 70 30 110 18 C150 8 190 24 240 14 C290 4 330 20 380 10 C430 2 470 22 520 12 C560 6 585 16 604 10 L604 305 L0 305 Z" fill="url(#sandTone)"/>
    </svg>
    <span class="pouch__notch pouch__notch--left"></span>
    <span class="pouch__notch pouch__notch--right"></span>
    <div class="pouch__zip"></div>

    <h1 class="headline">
      <span class="headline__lead">THE</span>
      <span class="headline__line headline__line--ocean">OCEAN</span>
      <span class="headline__line headline__line--healed">HEALED</span>
      <span class="headline__line headline__line--bag">MY A BAG</span>
    </h1>

    <p class="blurb">
      Lorem ipsum dolor sit amet, consectetuer<br>
      adipiscing elit, sed diam nonummy<br>
      nibh euismod tincidunt ut laoreet dolore<br>
      magna aliquam erat volutpat.
    </p>

    <p class="brand">TIDEWELL</p>
    <p class="product-line">OCEAN | IN A BAG</p>
    <p class="product-code">B77 6.1119</p>
    <p class="product-type">BATH SOAK</p>
  </main>
</body>
</html>
```